Mens Jewellery Homepage - Modern, Stylish Mens Ring Brand - Homepage

Project Overview: TorvikRings.com is a men's accessories brand specializing in high-quality mens rings.

The objective of this redesign is to create a modern, visually appealing homepage that is easy to navigate, showcases a wide range of rings, highlights personalization options, and builds trust with customers.

The new design should make a strong impression while reflecting the brand's premium quality and commitment to craftsmanship.

The focus will be on a sleek aesthetic that aligns with the tastes of men shopping for wedding bands, engagement rings, or fashion accessories.

Objectives:

Modern and Sleek Aesthetic:

A clean, minimalist design that emphasizes high-quality product imagery and thoughtful use of space.
Contemporary color palette that conveys elegance and sophistication, with accents that highlight key elements without overwhelming the user.

Consistent and easy-to-read typography that reflects the brand’s modern and masculine identity.

Showcasing Products:
Hero Section: A image to show off 3 or 4 ring designs that could be used for weddings or fashion.

Product Highlights: Below the hero banner, showcase product categories by color (see current website for colors)

Featured Products: Display a selection of “Top Rated” or “Customer Favorites” rings to help guide users toward popular choices.

Personalization Section:
A dedicated section promoting the ability to personalize rings, emphasizing features like engraving with names, dates, or special messages.
Include lifestyle images of personalized rings to inspire customers and give them an idea of what’s possible.
Use callouts such as “Make It Yours” or “Personalize Your Ring” to encourage users to explore the customization options available for each product.

Building Trust:

A space to show 5 or 6 testimonials and other trust elements

Symbols / text to show

free delivery
free returns
every ring stock
fast delivery
customer images (from reviews)

Driving Conversions:
Include a prominent call-to-action (CTA) button in the hero section with text like “Shop Now” or “Discover Our Collections.”

User Experience:
Fast, easy-to-navigate layout with simple and intuitive categories. Product categories and main sections should be clearly visible and easy to access without overwhelming the user.
Design the homepage to feel cohesive and uncluttered, with a logical flow from product discovery to personalization and checkout.

Visual Elements and Imagery:
Use ring images from our site, but add backgrounds etc to make the image on the homepage more interesting.

Personalization Options: Use visual representations (like ring mockups) showing where personalization options (such as engravings) would appear on the product.

I like (and would like to see some different designs from our current design)
Brisk.com for design
stoutloops.com

Target Market(s)

Men - 20 to 35

Number of Pages Required

1 page

Requirements
Must have
• Easy navigation, Trust, Modern, Clean,
Nice to have
• Would like to see Different designs like Brisk.com - StoutLoops.com

```html
<!DOCTYPE html>
<html lang="en">
<head>
<meta charset="utf-8">
<title>Torvik Rings — Men's Rings</title>
<link href="https://fonts.googleapis.com/css2?family=Prata&family=Jost:wght@400;500;600&display=swap" rel="stylesheet">
<style>
:root{
  --teal:#0b8580;
  --ink:#1d1d1d;
  --card:#f5f5f5;
  --line:#dcdcdc;
  --footer:#0e0e0e;
  --white:#ffffff;
}
*{margin:0;padding:0;box-sizing:border-box}
html,body{width:1200px;height:3563px;overflow:hidden}
body{position:relative;font-family:'Jost',sans-serif;color:var(--ink);background:var(--white)}
.abs{position:absolute}
.serif{font-family:'Prata',serif;font-weight:400}

.hero{left:0;top:0;width:1200px;height:592px;background:radial-gradient(ellipse at 30% 40%,#ffffff 0%,#eef0f2 55%,#dfe3e6 100%)}
.brand{display:flex;align-items:center;gap:12px;left:62px;top:40px}
.brand-circle{width:72px;height:72px;border:5px solid #2e2e2e;border-radius:50%}
.brand-name{font-size:24px;letter-spacing:8px;line-height:1.1;color:#2e2e2e;font-weight:500}
.nav{top:62px;left:602px;display:flex;gap:36px;font-size:18px}
.nav-icon{top:60px;width:30px;height:30px;border-radius:50%;background:var(--white);display:flex;align-items:center;justify-content:center;box-shadow:0 1px 4px rgba(0,0,0,.08)}
.hero-title{left:62px;top:200px;font-size:60px;line-height:80px;color:var(--teal)}
.hero-text{left:62px;top:380px;width:600px;font-size:18.5px;line-height:21px;color:#444;letter-spacing:.4px}
.btn-teal{background:var(--teal);color:var(--white);font-size:18px;display:flex;align-items:center;justify-content:center}
.hero-cta{left:62px;top:463px;width:231px;height:42px}
.arch{left:729px;top:177px;width:333px;height:415px;background:var(--teal);border-radius:167px 167px 0 0;overflow:hidden}
.arch-photo{position:absolute;left:70px;top:30px;width:190px;height:385px;background:linear-gradient(180deg,#e7b58f,#d89c74 60%,#c98a63);border-radius:90px 90px 0 0;opacity:.85}

.section-title{left:0;width:1200px;text-align:center;font-size:44px;color:var(--teal)}
.arrows{display:flex;gap:12px}
.arrow{width:40px;height:40px;border:1.5px solid #222;border-radius:50%;display:flex;align-items:center;justify-content:center}

.card{background:var(--card)}
.card-title{position:absolute;left:0;right:0;text-align:center;font-size:20px;letter-spacing:.6px}
.fav{position:absolute;top:28px;right:22px;width:32px;height:32px;border-radius:50%;background:var(--white);display:flex;align-items:center;justify-content:center}
.ring-photo{position:absolute;left:50%;transform:translateX(-50%);border-radius:50%}
.card-btn{position:absolute;left:50%;transform:translateX(-50%);background:var(--white);height:39px;display:flex;align-items:center;justify-content:center;font-size:17px;letter-spacing:.5px}

.engrave{left:62px;top:1808px;width:1074px;height:470px;background:var(--teal)}
.engrave-frame{left:35px;top:40px;width:412px;height:392px;background:var(--white)}
.engrave-photo{left:56px;top:61px;width:418px;height:350px;background:linear-gradient(135deg,#1f2740,#2c3552 45%,#e6c2a8 60%,#1c2236)}
.engrave-title{left:540px;width:460px;top:200px;text-align:center;color:var(--white);font-size:29px;font-weight:600;line-height:41px;letter-spacing:1px}
.engrave-btn{left:662px;top:328px;width:238px;height:39px;background:var(--white);font-size:18px;display:flex;align-items:center;justify-content:center;letter-spacing:.5px}

.review{top:2458px;width:210px;height:362px;border:1.5px solid var(--line);background:var(--white)}
.review-head{height:96px;border-bottom:1px solid var(--line);display:flex;align-items:center;justify-content:center;gap:16px;font-size:13px;font-weight:500}
.avatar{width:30px;height:30px;border-radius:50%;background:#555;color:var(--white);font-size:7px;display:flex;align-items:center;justify-content:center}
.review-text{position:absolute;top:140px;left:22px;right:22px;text-align:center;font-size:12.5px;line-height:16px;color:#333}
.review-meta{position:absolute;top:256px;left:16px;right:16px;display:flex;justify-content:space-between;font-size:12.5px;color:#777}
.review-meta b{color:#222;font-weight:500}
.review-meta .star{color:var(--teal)}
.review-btn{position:absolute;left:18px;right:18px;top:302px;height:40px;background:var(--teal);color:var(--white);font-size:17px;display:flex;align-items:center;justify-content:space-between;padding:0 18px}

.perks{left:0;top:2892px;width:1200px;height:329px;background:var(--teal)}
.perk{position:absolute;top:88px;width:260px;text-align:center;color:var(--white);font-size:20px;font-weight:600;letter-spacing:1px}
.perk-icon{width:96px;height:96px;border-radius:50%;background:var(--white);margin:0 auto 38px;display:flex;align-items:center;justify-content:center}

.footer{left:0;top:3221px;width:1200px;height:342px;background:var(--footer);color:#e6e6e6}
.footer .brand-circle{border-color:var(--white)}
.footer .brand-name{color:var(--white)}
.footer-info{left:66px;top:168px;font-size:11.5px;line-height:20px}
.footer-head{font-size:17px;color:var(--teal)}
.footer-list{list-style:none;font-size:11.5px;line-height:20px;margin-top:18px}
.footer-list li::before{content:"• ";}
.footer-bar{left:0;top:276px;width:1200px;border-top:1px solid #2a2a2a}
.pay{display:flex;gap:8px}
.pay span{width:28px;height:15px;border-radius:3px;background:#d9d9d9}
.footer-small{font-size:11.5px}
</style>
</head>
<body>

<section class="hero abs">
  <div class="brand abs">
    <div class="brand-circle"></div>
    <div class="brand-name">TORVIK<br>RINGS</div>
  </div>
  <nav class="nav abs">
    <span>Shop By Material</span><span>Shop By Color</span><span>Try At Home</span>
  </nav>
  <div class="nav-icon abs" style="left:1052px">
    <svg width="14" height="14" viewBox="0 0 24 24" fill="none" stroke="#222" stroke-width="2"><path d="M2 3h3l3 12h11l2-8H7"/><circle cx="9" cy="20" r="1.5"/><circle cx="18" cy="20" r="1.5"/></svg>
  </div>
  <div class="nav-icon abs" style="left:1109px">
    <svg width="14" height="14" viewBox="0 0 24 24" fill="none" stroke="#222" stroke-width="2"><circle cx="12" cy="8" r="4"/><path d="M4 21c1-5 15-5 16 0"/></svg>
  </div>

  <h1 class="hero-title abs serif">Elevate Your Style<br>With Torvik Rings</h1>
  <p class="hero-text abs">our selection of gold rings are here for the classic man. Inventive, modern and unique twists on a traditional gold ring.</p>
  <a class="hero-cta btn-teal abs">Discover Our Collections</a>

  <div class="arch abs">
    <div class="arch-photo" role="img" aria-label="Hand wearing stacked rings and bracelets"></div>
  </div>
</section>

<h2 class="section-title abs serif" style="top:654px">Product</h2>
<div class="arrows abs" style="left:1046px;top:671px">
  <span class="arrow"><svg width="18" height="12" viewBox="0 0 18 12" fill="none" stroke="#222" stroke-width="1.5"><path d="M17 6H1M6 1L1 6l5 5"/></svg></span>
  <span class="arrow"><svg width="18" height="12" viewBox="0 0 18 12" fill="none" stroke="#222" stroke-width="1.5"><path d="M1 6h16M12 1l5 5-5 5"/></svg></span>
</div>

<div class="card abs" style="left:62px;top:777px;width:354px;height:373px">
  <div class="card-title" style="top:26px;text-align:left;left:28px">Black Rings for Men</div>
  <span class="fav"><svg width="14" height="13" viewBox="0 0 24 22" fill="none" stroke="#222" stroke-width="2"><path d="M12 20S2 13 2 7a5 5 0 0 1 10-1 5 5 0 0 1 10 1c0 6-10 13-10 13z"/></svg></span>
  <div class="ring-photo" role="img" aria-label="Black tungsten ring" style="top:110px;width:110px;height:150px;background:radial-gradient(ellipse,#555 0%,#111 70%)"></div>
  <div class="card-btn" style="top:304px;width:285px">View All Product</div>
</div>
<div class="card abs" style="left:426px;top:777px;width:352px;height:373px">
  <div class="card-title" style="top:30px;text-align:left;left:32px">Silver Rings for Men</div>
  <span class="fav"><svg width="14" height="13" viewBox="0 0 24 22" fill="none" stroke="#222" stroke-width="2"><path d="M12 20S2 13 2 7a5 5 0 0 1 10-1 5 5 0 0 1 10 1c0 6-10 13-10 13z"/></svg></span>
  <div class="ring-photo" role="img" aria-label="Brushed silver ring" style="top:118px;width:105px;height:142px;background:radial-gradient(ellipse,#f2f2f2 0%,#a9a9a9 70%)"></div>
  <div class="card-btn" style="top:304px;width:285px">View All Product</div>
</div>
<div class="card abs" style="left:788px;top:777px;width:354px;height:373px">
  <div class="card-title" style="top:30px;text-align:left;left:28px">Gold Rings for Men</div>
  <span class="fav"><svg width="14" height="13" viewBox="0 0 24 22" fill="none" stroke="#222" stroke-width="2"><path d="M12 20S2 13 2 7a5 5 0 0 1 10-1 5 5 0 0 1 10 1c0 6-10 13-10 13z"/></svg></span>
  <div class="ring-photo" role="img" aria-label="Polished gold ring" style="top:110px;width:100px;height:146px;background:radial-gradient(ellipse,#fff2b0 0%,#d4a92a 70%)"></div>
  <div class="card-btn" style="top:304px;width:285px">View All Product</div>
</div>

<h2 class="section-title abs serif" style="top:1232px">Featured Product</h2>
<div class="arrows abs" style="left:1046px;top:1249px">
  <span class="arrow"><svg width="18" height="12" viewBox="0 0 18 12" fill="none" stroke="#222" stroke-width="1.5"><path d="M17 6H1M6 1L1 6l5 5"/></svg></span>
  <span class="arrow"><svg width="18" height="12" viewBox="0 0 18 12" fill="none" stroke="#222" stroke-width="1.5"><path d="M1 6h16M12 1l5 5-5 5"/></svg></span>
</div>

<div class="card abs" style="left:62px;top:1355px;width:261px;height:373px">
  <div class="card-title" style="top:34px">Blue Rings for Men</div>
  <div class="ring-photo" role="img" aria-label="Blue and silver ring" style="top:125px;width:105px;height:142px;background:radial-gradient(ellipse,#c9d3e6 0%,#1f4fb8 70%)"></div>
  <div class="card-btn" style="top:310px;width:207px">View All Product</div>
</div>
<div class="card abs" style="left:333px;top:1355px;width:261px;height:373px">
  <div class="card-title" style="top:34px">Titanium - Rose gold</div>
  <div class="ring-photo" role="img" aria-label="Rose gold and titanium ring" style="top:125px;width:100px;height:146px;background:radial-gradient(ellipse,#eee 0%,#d4956a 70%)"></div>
  <div class="card-btn" style="top:310px;width:207px">View All Product</div>
</div>
<div class="card abs" style="left:604px;top:1355px;width:261px;height:373px">
  <div class="card-title" style="top:34px">Brown Wedding Rings</div>
  <div class="ring-photo" role="img" aria-label="Silver ring with wood inlay" style="top:122px;width:100px;height:146px;background:radial-gradient(ellipse,#e8e8e8 0%,#7a3a22 70%)"></div>
  <div class="card-btn" style="top:310px;width:207px">View All Product</div>
</div>
<div class="card abs" style="left:875px;top:1355px;width:261px;height:373px">
  <div class="card-title" style="top:34px">Gold Rings for Men</div>
  <div class="ring-photo" role="img" aria-label="Polished gold ring" style="top:122px;width:100px;height:150px;background:radial-gradient(ellipse,#fff2b0 0%,#d4a92a 70%)"></div>
  <div class="card-btn" style="top:310px;width:207px">View All Product</div>
</div>

<section class="engrave abs">
  <div class="engrave-frame abs"></div>
  <div class="engrave-photo abs" role="img" aria-label="Groom placing a wedding ring, with flowers"></div>
  <h2 class="engrave-title abs">Personalize Your Ring with<br>Unique Engravings</h2>
  <a class="engrave-btn abs">Make It Yours</a>
</section>

<h2 class="section-title abs serif" style="top:2340px">Testimonials</h2>
<div class="arrows abs" style="left:1046px;top:2346px">
  <span class="arrow"><svg width="18" height="12" viewBox="0 0 18 12" fill="none" stroke="#222" stroke-width="1.5"><path d="M17 6H1M6 1L1 6l5 5"/></svg></span>
  <span class="arrow"><svg width="18" height="12" viewBox="0 0 18 12" fill="none" stroke="#222" stroke-width="1.5"><path d="M1 6h16M12 1l5 5-5 5"/></svg></span>
</div>

<article class="review abs" style="left:59px">
  <div class="review-head"><span class="avatar">OH</span>Owen Hartley</div>
  <p class="review-text">Fan wedding ring substitute for when husband is at work</p>
  <div class="review-meta"><b>5 <span class="star">★</span></b><span>3 days ago</span></div>
  <a class="review-btn">View<svg width="24" height="12" viewBox="0 0 24 12" fill="none" stroke="#fff" stroke-width="1.5"><path d="M0 6h23M18 1l5 5-5 5"/></svg></a>
</article>
<article class="review abs" style="left:278px">
  <div class="review-head"><span class="avatar">SK</span>Sam Keller</div>
  <p class="review-text">I love the idea of a silicone ring, very clever idea!<br>It is very comfortable to wear...</p>
  <div class="review-meta"><b>5 <span class="star">★</span></b><span>4 days ago</span></div>
  <a class="review-btn">View<svg width="24" height="12" viewBox="0 0 24 12" fill="none" stroke="#fff" stroke-width="1.5"><path d="M0 6h23M18 1l5 5-5 5"/></svg></a>
</article>
<article class="review abs" style="left:496px">
  <div class="review-head"><span class="avatar">DW</span>Dean Whitford</div>
  <p class="review-text">My ring is fantastic and super fast delivery. Nora was superb, making ...</p>
  <div class="review-meta"><b>5 <span class="star">★</span></b><span>2 days ago</span></div>
  <a class="review-btn">View<svg width="24" height="12" viewBox="0 0 24 12" fill="none" stroke="#fff" stroke-width="1.5"><path d="M0 6h23M18 1l5 5-5 5"/></svg></a>
</article>
<article class="review abs" style="left:715px">
  <div class="review-head"><span class="avatar">AC</span>Amy Corran</div>
  <p class="review-text">Gorgeous silver wedding band, my partner fell in love with it so worth the money...</p>
  <div class="review-meta"><b>5 <span class="star">★</span></b><span>2 days ago</span></div>
  <a class="review-btn">View<svg width="24" height="12" viewBox="0 0 24 12" fill="none" stroke="#fff" stroke-width="1.5"><path d="M0 6h23M18 1l5 5-5 5"/></svg></a>
</article>
<article class="review abs" style="left:933px">
  <div class="review-head"><span class="avatar">TM</span>Tessa Marlow</div>
  <p class="review-text">Fan wedding ring substitute for when husband is at work ...</p>
  <div class="review-meta"><b>5 <span class="star">★</span></b><span>3 days ago</span></div>
  <a class="review-btn">View<svg width="24" height="12" viewBox="0 0 24 12" fill="none" stroke="#fff" stroke-width="1.5"><path d="M0 6h23M18 1l5 5-5 5"/></svg></a>
</article>

<section class="perks abs">
  <div class="perk" style="left:65px">
    <div class="perk-icon"><svg width="50" height="40" viewBox="0 0 50 40" fill="none" stroke="#222" stroke-width="2"><rect x="4" y="10" width="28" height="20"/><path d="M32 16h8l6 7v7H32z"/><circle cx="12" cy="33" r="4"/><circle cx="38" cy="33" r="4"/></svg></div>
    Free delivery
  </div>
  <div class="perk" style="left:336px">
    <div class="perk-icon"><svg width="46" height="46" viewBox="0 0 46 46" fill="none" stroke="#222" stroke-width="2"><path d="M8 23a15 15 0 0 1 27-9M38 23a15 15 0 0 1-27 9"/><path d="M35 6v8h-8M11 40v-8h8"/><rect x="17" y="17" width="12" height="12"/></svg></div>
    Free returns
  </div>
  <div class="perk" style="left:627px">
    <div class="perk-icon"><svg width="48" height="44" viewBox="0 0 48 44" fill="none" stroke="#222" stroke-width="2"><rect x="16" y="4" width="14" height="14"/><rect x="6" y="22" width="14" height="14"/><rect x="24" y="22" width="14" height="14"/><path d="M34 10l4 4 7-8"/></svg></div>
    Every ring stock
  </div>
  <div class="perk" style="left:888px">
    <div class="perk-icon"><svg width="50" height="40" viewBox="0 0 50 40" fill="none" stroke="#222" stroke-width="2"><path d="M2 14h10M0 20h12"/><rect x="14" y="8" width="20" height="22"/><path d="M34 14h7l6 8v8H34z"/><circle cx="21" cy="33" r="4"/><circle cx="41" cy="33" r="4"/></svg></div>
    Fast delivery
  </div>
</section>

<footer class="footer abs">
  <div class="brand abs" style="left:66px;top:52px">
    <div class="brand-circle" style="width:76px;height:76px"></div>
    <div class="brand-name" style="font-size:26px">TORVIK<br>RINGS</div>
  </div>
  <div class="footer-info abs">© 2024 Torvik Rings · 14B Ferry Lane, Alderby, AL7 3QP<br>Contact 01632 480215 · nora@torvikrings.com<br>Halvard Trading Ltd · 09381542 · Incorporated on 20 April 2001</div>
  <div class="abs" style="left:516px;top:60px">
    <div class="footer-head">Quick Links</div>
    <ul class="footer-list">
      <li>FREE ring sizer</li><li>FREE Delivery | Returns and Exchanges</li><li>Try at Home</li><li>Ring Engraving</li><li>Contact Us</li><li>Blog</li>
    </ul>
  </div>
  <div class="abs" style="left:825px;top:60px">
    <div class="footer-head">Ring Guide</div>
    <ul class="footer-list">
      <li>The Best Tungsten and Titanium Rings - Full Guide</li><li>How is Tungsten or Titanium Ring Size Measured?</li><li>Black, Silver Gold - The best colors for mens tungsten</li><li>and titanium rings</li><li>Whats better tungsten or titanium for a mens ring</li>
    </ul>
  </div>
  <div class="footer-bar abs"></div>
  <div class="footer-small abs" style="left:66px;top:300px">© Copyright 2024 All Rights Reserved.</div>
  <div class="pay abs" style="left:462px;top:300px"><span></span><span></span><span></span><span></span><span></span><span></span><span></span><span></span></div>
  <div class="footer-small abs" style="left:934px;top:300px">Privacy policy</div>
  <div class="footer-small abs" style="left:1044px;top:300px">Terms of Service</div>
</footer>

</body>
</html>
```